Web Design Nutrition supplements (Quillstack 5 pages)

We are looking for templates for a new nutrition supplement shop www.velmorida.ch , targeting Swiss Female 65% /Male 35% over 40 yrs with high quality products (no performance enhancement /Body building products).
Our customers are not the most proficient in internet, so the website should be simple, easily understood. not too much web2.0 look and feel and functionality.

velmorida.ch product offerings are high quality and supplied from top brands: like Dr. Wentholm, Soravin, talbrücken, Nalvimed), for diets, weight management, antistress, anti-apathy, oligo-elements, omega-3 oils, and cosmetics.

We want the website design
1) to reflect our seriousness and expertise in the area,
2)to Inspire trust from our customers and address their needs in a personal and professional way (we answer your questions over email/Phone)
3) though we are not an pharmacy, our products are currently sold in pharmacies in Switzerland, so we want our customers to feel as well served online, as if they were in a pharmacy.
4) compare favorably to international websites (F, G) also selling online to Swiss customers: we are a truly Swiss company and can deliver within less than 18 h. in Switzerland (so the Swiss flag is an important design element for us)

We want to provide a superior buying experience,
1) important: providing sufficient product information: (intelligible snippet/summary of product info) should be visible on search result pages, and category pages,
2) clarity of design "emphasis" on products with clear call to action (buy)

Deliverables for the winning designer;
Photoshop files that can be easily be integrated in our quillstack shop.
- Homepage
- Category Page
- Product Page
For 1st evaluation and corrections of the proposals.

- Landing Page (for SEM Campaigns)
- Newsletter (Post raven)
as a second step.

Please use the attached wireframes, that should give you the exact content we want to provide (as well as functionality), the wireframes donnot define the user experience/design (it s more like a guidance, suggestion)

Target Market(s)

Swiss Males /35% Females 65% (both Swiss French/ Swiss German over 40 years

Industry/Entity Type

Nutrition

Requirements
Must have
• Deliverables:
- Homepage
- Category Page
- Product Page

- Newsletter template
- Landing Page

We attach:
- navigation to show how users can access the products (cat/ sub cat, but also search for body parts, objectives of healing... (see Kategorien-for-web.xls)
- Wireframes (myKrondelo)
- Logo (1 psd)
- Product images (zip files)
- Benchmarks: vitorelle.co.uk (simplicity), pmv.com (expandable navigation),
- Competitors: ko7.de, tramelo.com, tramelo-deutschland.de, quint-fold.eu

```html
<!DOCTYPE html>
<html lang="de">
<head>
<meta charset="utf-8">
<title>velmorida – Warenkorb</title>
<link href="https://fonts.googleapis.com/css2?family=Dosis:wght@400;500;600;700&display=swap" rel="stylesheet">
<style>
:root{
  --navy:#1b3a72;
  --navy-dark:#132c5a;
  --lime:#cfe58a;
  --lime-light:#e4f2b0;
  --blue-tab:#2a63c9;
  --page-bg:#d8e7f8;
  --gutter:#e6e6e6;
  --line:#dcdcdc;
  --text:#333;
  --link:#2a5bb8;
  --price:#2fa12f;
  --orange:#f15a1f;
  --btn-blue:#8db4f2;
  --btn-grey:#8d9bb2;
  --footer-top:#8fb8ee;
  --footer-bottom:#c9def9;
}
*{box-sizing:border-box;margin:0;padding:0}
html,body{width:1200px;height:1000px;overflow:hidden}
body{font-family:"Dosis",sans-serif;color:var(--text);font-size:11px;position:relative;background:#3a4a3a}
.backdrop{position:absolute;inset:0;background:linear-gradient(90deg,#4b6b3c 0%,#2f3b30 12%,#6a4a4a 20%,#3c4b3a 80%,#5a3a3a 90%,#3b4a5a 100%)}
.shell{position:absolute;left:264px;top:0;width:671px;height:1000px;background:var(--gutter)}
.abs{position:absolute}
.topbar{left:0;top:0;width:671px;height:22px;background:var(--lime-light);font-size:10px}
.topbar span{position:absolute;top:5px;white-space:nowrap}
.flag{display:inline-block;width:12px;height:12px;border-radius:50%;vertical-align:-2px;margin-right:4px}
.header{left:0;top:22px;width:671px;height:74px;background:var(--navy)}
.brand{left:52px;top:20px;color:#fff;font-size:22px;font-weight:600;display:flex;align-items:center;gap:6px}
.brand i{width:14px;height:14px;border-radius:50%;background:#7fbf3f;display:block}
.usp{color:#fff;font-size:10px;line-height:11px;display:flex;gap:6px;align-items:center;white-space:nowrap}
.usp svg{flex:none}
.search{left:234px;top:48px;width:182px;height:17px;background:#fff;border:1px solid #ccc}
.search-btn{left:416px;top:48px;width:16px;height:17px;background:#4aa43a}
.cart-btn{left:490px;top:26px;width:64px;height:23px;border:1px solid #fff;background:var(--blue-tab);color:#fff;font-size:9px;line-height:9.5px;padding:1px 3px;white-space:nowrap;font-weight:500}
.bag{left:582px;top:6px;width:22px;height:32px;background:#2fbf3a;border-radius:2px}
.help{left:576px;top:56px;color:#8fd0ff;font-size:9px;text-decoration:underline}
.help-dot{left:596px;top:54px;width:14px;height:14px;border:1px solid #8fd0ff;border-radius:50%;color:#8fd0ff;font-size:9px;text-align:center;line-height:12px}
.nav{left:0;top:96px;width:671px;height:30px;background:var(--lime);display:flex;align-items:center;padding-left:47px;font-size:9.8px}
.nav a{flex:none;white-space:nowrap;padding:0 3px;border-right:1px solid #9db55a;height:30px;line-height:30px;color:#222;text-decoration:none}
.nav a.active{background:var(--blue-tab);color:#fff}
.main{left:52px;top:126px;width:561px;height:704px;background:var(--page-bg)}
.crumbs{left:60px;top:132px;font-size:8px}
.crumbs a{color:var(--link);text-decoration:none}
.card{background:#fff;border:1px solid var(--line)}
.cart{left:61px;top:151px;width:538px;height:299px}
.th{position:absolute;top:0;height:19px;line-height:19px;font-size:8px;border-left:1px solid var(--line);text-align:center;white-space:nowrap}
.row{position:absolute;left:0;width:536px;height:121px;border-top:1px solid var(--line)}
.row .cell{position:absolute;top:0;height:120px;border-left:1px solid var(--line);font-size:8px;text-align:center}
.thumb{position:absolute;left:28px;top:14px;width:40px;height:56px;border-radius:4px;background:linear-gradient(#f4f4f4,#e07a2a 45%,#f4f4f4 70%,#7bb33a)}
.pname{font-weight:600;font-size:9px;color:#222;white-space:nowrap}
.pqty{font-size:8px}
.pprice{color:var(--price);font-weight:700;font-size:9px}
.qty{display:inline-block;width:24px;height:12px;border:1px solid #ccc;font-size:7px;line-height:10px;margin-top:45px}
.actions{left:61px;top:412px;width:538px;height:38px;background:#f2f2f2;border:1px solid var(--line)}
.mini-btn{position:absolute;top:10px;height:16px;background:#fafafa;border:1px solid var(--line);font-size:7.5px;line-height:14px;padding:0 8px;white-space:nowrap}
.coupon{left:61px;top:450px;width:340px;height:92px;background:#ececec}
.coupon-in{left:18px;top:20px;width:108px;height:17px;background:#f4f4f4;border:1px solid #bbb;font-size:7.5px;line-height:15px;padding-left:10px;white-space:nowrap}
.coupon-btn{left:20px;top:46px;width:106px;height:17px;background:var(--btn-blue);color:#fff;font-size:8px;line-height:17px;text-align:center}
.totals{left:401px;top:450px;width:198px;height:92px;background:#e4e4e4;font-size:8px;padding:16px 30px 0 40px;line-height:10px}
.totals .l{display:flex;justify-content:space-between}
.totals .sum{font-weight:700;margin-top:10px}
.order{left:401px;top:542px;width:198px;height:38px;background:var(--orange);color:#fff;font-size:12.5px;font-weight:600;text-align:center;line-height:38px;white-space:nowrap}
.info{left:61px;top:588px;width:538px;height:64px;font-size:8.5px;padding:9px 10px}
.badge{position:absolute;top:25px;width:28px;height:32px;background:#8a8a8a;border-radius:3px 3px 14px 14px}
.recs{left:61px;top:656px;width:538px;height:161px}
.recs h2{font-size:13px;font-weight:500;position:absolute;left:9px;top:4px;white-space:nowrap}
.rec{position:absolute;top:28px;width:104px;height:130px;text-align:center;border-right:1px solid var(--line)}
.rec .thumb{left:32px;top:0}
.rec .meta{position:absolute;top:60px;left:0;width:100%;line-height:11px}
.rec .add{display:inline-block;margin-top:5px;width:44px;height:17px;background:var(--btn-grey);color:#fff;font-size:8px;line-height:17px}
.rec .wish{display:block;margin-top:3px;color:var(--link);font-size:7.5px;text-decoration:underline;white-space:nowrap}
.footer{left:0;top:830px;width:671px;height:170px;background:linear-gradient(var(--footer-top),var(--footer-bottom));font-size:8.5px}
.footer a{color:#222;text-decoration:underline}
.fcol{position:absolute;top:46px;line-height:14.5px}
.fcol a{display:block;white-space:nowrap}
.social{position:absolute;top:130px;width:14px;height:14px;background:#3b6db8}
</style>
</head>
<body>
<div class="backdrop" role="img" aria-label="Blurred pharmacy shelves with supplement packages"></div>
<div class="shell">
  <div class="abs topbar">
    <span style="left:64px"><i class="flag" style="background:#e0a52a"></i>DE</span>
    <span style="left:100px"><i class="flag" style="background:linear-gradient(90deg,#2a4db8 33%,#fff 33% 66%,#d33 66%)"></i><u>FR</u></span>
    <span style="left:259px">Hallo <b>Franzi</b></span>
    <span style="left:311px;color:var(--link)">(<u>Bind Bie nicht Franzi?</u>)</span>
    <span style="left:553px"><u>Mein Konto</u></span>
  </div>

  <div class="abs header">
    <div class="abs brand"><i></i>velmorida</div>
    <div class="abs usp" style="left:186px;top:10px">
      <svg width="18" height="18"><circle cx="9" cy="9" r="8" fill="none" stroke="#8fb0e0" stroke-width="1.5"/><path d="M9 4v5h4" stroke="#8fb0e0" fill="none" stroke-width="1.5"/></svg>
      <span>18 Std. Lieferung<br>in der Schweiz</span></div>
    <div class="abs usp" style="left:286px;top:10px">
      <svg width="18" height="18"><circle cx="9" cy="9" r="8" fill="none" stroke="#8fb0e0" stroke-width="1.5"/><text x="9" y="12" font-size="7" fill="#8fb0e0" text-anchor="middle">CHF</text></svg>
      <span>Gratisversand<br>ab 80 CHF</span></div>
    <div class="abs usp" style="left:372px;top:10px">
      <svg width="22" height="18"><rect x="2" y="4" width="5" height="12" fill="#8fb0e0"/><rect x="8.5" y="4" width="5" height="12" fill="#8fb0e0"/><rect x="15" y="4" width="5" height="12" fill="#8fb0e0"/></svg>
      <span>Experten Beratung</span></div>
    <div class="abs search"></div>
    <div class="abs search-btn"><svg width="16" height="17"><circle cx="7.5" cy="7.5" r="3.5" fill="none" stroke="#fff" stroke-width="1.5"/><path d="M10 10l3 3" stroke="#fff" stroke-width="1.5"/></svg></div>
    <div class="abs cart-btn">Zum Warenkorb<br>12,90 CHF</div>
    <div class="abs bag"></div>
    <div class="abs help">hilfe</div>
    <div class="abs help-dot">?</div>
  </div>

  <nav class="abs nav">
    <a>Vitamins</a><a>Mineralien</a><a>Essentielle Fettsäure</a><a class="active">Prä-Probiotika</a><a>Spirulina-Maca</a><a>Gewichtsabnahme</a><a>Kosmetik</a><a>Phytotherapie</a><a>funktionelle Nahrung</a><a style="border:0">ANGEBOTE</a>
  </nav>

  <div class="abs main"></div>
  <div class="abs crumbs"><a>Home</a> &gt; <a>Kategorien</a> &gt; Produkt</div>

  <div class="abs card cart">
    <div class="th" style="left:0;width:340px;text-align:left;padding-left:16px;border:0">Artikelname</div>
    <div class="th" style="left:340px;width:48px">Einzelpreis</div>
    <div class="th" style="left:388px;width:31px">Stück</div>
    <div class="th" style="left:419px;width:44px">Entfernen</div>
    <div class="th" style="left:463px;width:73px">Zwischensumme</div>
    <div class="row" style="top:19px">
      <div class="thumb" role="img" aria-label="Spirulina 250mg bottle with BIO badge"></div>
      <div class="abs" style="left:0;top:74px;width:96px;text-align:center;line-height:11px"><div class="pname">Spirulina 250mg</div><div class="pqty">120 Stücke</div><div class="pprice">36,77 SFR</div></div>
      <div class="abs" style="left:98px;top:47px;font-size:8.5px;white-space:nowrap">Omega 3 planzlich, Kapeseln, 120 Stück</div>
      <div class="cell" style="left:340px;width:48px;line-height:102px">45,5 CHF</div>
      <div class="cell" style="left:388px;width:31px"><span class="qty">1</span></div>
      <div class="cell" style="left:419px;width:44px"><svg width="14" height="18" style="margin-top:40px"><rect x="2" y="4" width="10" height="13" fill="none" stroke="#aaa"/><path d="M0 3h14M5 1h4" stroke="#aaa"/></svg></div>
      <div class="cell" style="left:463px;width:73px;line-height:102px">45,5 CHF</div>
    </div>
    <div class="row" style="top:140px">
      <div class="thumb" role="img" aria-label="Spirulina 250mg bottle with BIO badge"></div>
      <div class="abs" style="left:0;top:74px;width:96px;text-align:center;line-height:11px"><div class="pname">Spirulina 250mg</div><div class="pqty">120 Stücke</div><div class="pprice">36,77 SFR</div></div>
      <div class="abs" style="left:98px;top:47px;font-size:8.5px;white-space:nowrap">Omega 3 planzlich, Kapeseln, 120 Stück</div>
      <div class="cell" style="left:340px;width:48px;line-height:102px">45,5 CHF</div>
      <div class="cell" style="left:388px;width:31px"><span class="qty">1</span></div>
      <div class="cell" style="left:419px;width:44px"><svg width="14" height="18" style="margin-top:40px"><rect x="2" y="4" width="10" height="13" fill="none" stroke="#aaa"/><path d="M0 3h14M5 1h4" stroke="#aaa"/></svg></div>
      <div class="cell" style="left:463px;width:73px;line-height:102px">45,5 CHF</div>
    </div>
  </div>

  <div class="abs actions">
    <div class="mini-btn" style="left:334px">Update Shopping Cart</div>
    <div class="mini-btn" style="left:435px">Clear Shopping Cart</div>
  </div>

  <div class="abs coupon">
    <div class="abs coupon-in">Bitte Gutscheincode eingeben</div>
    <div class="abs coupon-btn">Gutschein einlösen</div>
  </div>
  <div class="abs totals">
    <div class="l"><span>Zwischensumme</span><span>91,0 SFr</span></div>
    <div class="l"><span>Versand &amp; Bearbeitung</span><span>7,5 SFr</span></div>
    <div class="l"><span>Inkl Umsatzsteuer</span><span>6,65 SFr</span></div>
    <div>(11included)</div>
    <div class="l sum"><span>Gesamtsumme</span><span>98,5 SFr</span></div>
  </div>
  <div class="abs order">Jetz Bestellen und zur Bezahlung</div>

  <div class="abs card info">
    <p>Schnelle Lieferung in der Schweiz, Kostenloser Versand ab 80 SFr, Sichere Bezahlung durch unsere Partner</p>
    <p style="margin-top:12px">Zahlungsmöglichkeiten:</p>
    <div class="badge" style="left:320px"></div>
    <div class="badge" style="left:372px"></div>
    <div class="badge" style="left:425px"></div>
    <div class="badge" style="left:473px"></div>
  </div>

  <div class="abs card recs">
    <h2>Andere Kunden fanden diese Artikel interessant!</h2>
    <div class="rec" style="left:8px"><div class="thumb" role="img" aria-label="Spirulina 250mg bottle"></div><div class="meta"><div class="pname">Spirulina 250mg</div><div class="pqty">120 Stücke</div><div class="pprice">36,77 SFR</div><span class="add">Warenkor</span><a class="wish">auf den Wurschzeitel</a></div></div>
    <div class="rec" style="left:112px"><div class="thumb" role="img" aria-label="Spirulina 250mg bottle"></div><div class="meta"><div class="pname">Spirulina 250mg</div><div class="pqty">120 Stücke</div><div class="pprice">36,77 SFR</div><span class="add">Warenkor</span><a class="wish">auf den Wurschzeitel</a></div></div>
    <div class="rec" style="left:216px"><div class="thumb" role="img" aria-label="Spirulina 250mg bottle"></div><div class="meta"><div class="pname">Spirulina 250mg</div><div class="pqty">120 Stücke</div><div class="pprice">36,77 SFR</div><span class="add">Warenkor</span><a class="wish">auf den Wurschzeitel</a></div></div>
    <div class="rec" style="left:320px"><div class="thumb" role="img" aria-label="Spirulina 250mg bottle"></div><div class="meta"><div class="pname">Spirulina 250mg</div><div class="pqty">120 Stücke</div><div class="pprice">36,77 SFR</div><span class="add">Warenkor</span><a class="wish">auf den Wurschzeitel</a></div></div>
    <div class="rec" style="left:424px;border:0"><div class="thumb" role="img" aria-label="Spirulina 250mg bottle"></div><div class="meta"><div class="pname">Spirulina 250mg</div><div class="pqty">120 Stücke</div><div class="pprice">36,77 SFR</div><span class="add">Warenkor</span><a class="wish">auf den Wurschzeitel</a></div></div>
  </div>

  <footer class="abs footer">
    <div class="abs" style="left:60px;top:22px;white-space:nowrap"><a>Impressum</a> &nbsp;|&nbsp; <a>Wer sind Wir?</a> &nbsp;|&nbsp; <a>Über uns</a> &nbsp;|&nbsp; <a>AGB's</a></div>
    <div class="fcol" style="left:60px"><a>KUNDENSERVICE</a><a>Kontakt</a><a>Lexikon Hilfe &amp; Antworten</a><a>Blog</a><a>Partnerprogramm</a><a>Reseller Program</a></div>
    <div class="fcol" style="left:179px"><a>NAVIGATIONSHILFE</a><a>Suchbegriffe</a><a>Marken</a><a>Erweiterte Suche</a><a>Sitemap</a></div>
    <div class="fcol" style="left:289px"><a>Das Unternehmen</a><a>Expertise</a><a>Jobs</a><a>User Team</a></div>
    <div class="social" style="left:534px;top:131px"></div>
    <div class="social" style="left:554px;top:131px;background:#5ab0e6"></div>
  </footer>
</div>
</body>
</html>
```